Harborline Restoration Business Card Design Phase 2

Professional and clean design. The design colors should flow with the logo. Two-sided card with the website on the back which is:

www.HarborlineRestoration.example.

"Specializing in Water Damage Restoration"

On the front I need the name, email, phone, and logo.

Name: Darnell Vickery
Email: Darnell@HarborlineRestoration.example
Phone: 555-018-2734 for now

I only have the Preview and Thumbnail right now but should have the source files uploaded within a day or two.

Target Market(s)

Flood victims, home owners with water damage from busted pipes etc...

Industry/Entity Type

Business

Contact Information for Business Card

Name: Darnell Vickery

Font styles to use
Serif
Sans Serif

Requirements
Must have
• Business Card Details Info

```html
<!DOCTYPE html>
<html lang="en">
<head>
<meta charset="utf-8">
<title>Harborline Restoration Business Card</title>
<link rel="stylesheet" href="https://fonts.googleapis.com/css2?family=Open+Sans:wght@400;700;800&display=swap">
<style>
  :root {
    --page: #3a3330;
    --card: #121213;
    --card-back: #0d0d0e;
    --brand-blue: #2d4a8c;
    --text-light: #e9e9ea;
    --rule: #cfcfd2;
    --tag: #d6d6d8;
  }
  * { box-sizing: border-box; margin: 0; padding: 0; }
  html, body { width: 1200px; height: 814px; overflow: hidden; }
  body {
    background: var(--page);
    font-family: "Open Sans", Arial, sans-serif;
    display: flex;
    align-items: center;
    justify-content: center;
    gap: 60px;
  }
  .card {
    width: 525px;
    height: 300px;
    position: relative;
    border-radius: 3px;
    box-shadow: 0 10px 24px rgba(0,0,0,0.45);
  }
  .card-front { background: var(--card); }
  .card-back { background: var(--card-back); }

  .front-brand {
    position: absolute;
    top: 34px;
    right: 34px;
    width: 210px;
    text-align: left;
    color: var(--brand-blue);
    font-weight: 800;
    font-size: 31px;
    line-height: 1.0;
    text-transform: uppercase;
    letter-spacing: -0.5px;
  }
  .front-rule {
    position: absolute;
    top: 122px;
    left: 150px;
    right: 34px;
    height: 1px;
    background: var(--rule);
  }
  .holder {
    position: absolute;
    left: 34px;
    bottom: 104px;
    color: var(--brand-blue);
    font-size: 19px;
    font-weight: 700;
  }
  .holder-rule {
    position: absolute;
    left: 34px;
    bottom: 95px;
    width: 190px;
    height: 1px;
    background: var(--rule);
  }
  .contact-list {
    position: absolute;
    left: 34px;
    bottom: 22px;
    list-style: none;
    color: var(--text-light);
    font-size: 14px;
    line-height: 23px;
  }
  .contact-list li { display: flex; align-items: center; gap: 10px; }
  .contact-list svg { width: 13px; height: 13px; fill: var(--brand-blue); flex: none; }

  .back-brand {
    position: absolute;
    top: 92px;
    left: 0;
    right: 0;
    text-align: center;
    color: var(--text-light);
    font-weight: 800;
    font-size: 36px;
    line-height: 1.0;
    text-transform: uppercase;
    letter-spacing: -0.5px;
  }
  .tagline {
    position: absolute;
    bottom: 62px;
    left: 40px;
    right: 40px;
    display: flex;
    align-items: center;
    gap: 8px;
    color: var(--tag);
    font-size: 12.5px;
    white-space: nowrap;
  }
  .tagline::before, .tagline::after {
    content: "";
    flex: 1;
    height: 1px;
    background: var(--rule);
  }
</style>
</head>
<body>
  <section class="card card-front" aria-label="Business card front">
    <div class="front-brand">Harborline Restoration</div>
    <div class="front-rule"></div>
    <p class="holder">Darnell Vickery</p>
    <div class="holder-rule"></div>
    <ul class="contact-list">
      <li>
        <svg viewBox="0 0 24 24" aria-hidden="true"><path d="M6.6 10.8a15.1 15.1 0 0 0 6.6 6.6l2.2-2.2a1 1 0 0 1 1-.25 11.4 11.4 0 0 0 3.6.57 1 1 0 0 1 1 1V20a1 1 0 0 1-1 1A17 17 0 0 1 3 4a1 1 0 0 1 1-1h3.5a1 1 0 0 1 1 1c0 1.25.2 2.45.57 3.57a1 1 0 0 1-.25 1z"/></svg>
        555-018-2734
      </li>
      <li>
        <svg viewBox="0 0 24 24" aria-hidden="true"><path d="M2 5h20v14H2z M4 7v.4l8 5 8-5V7l-8 5z" fill-rule="evenodd"/></svg>
        Darnell@HarborlineRestoration.example
      </li>
      <li>
        <svg viewBox="0 0 24 24" aria-hidden="true"><path d="M12 2a10 10 0 1 0 0 20 10 10 0 0 0 0-20zm0 2c.9 0 2.2 2 2.7 5H9.3C9.8 6 11.1 4 12 4zM4.3 11h3a17 17 0 0 0 0 2h-3a8 8 0 0 1 0-2zm5 0h5.4a15 15 0 0 1 0 2H9.3a15 15 0 0 1 0-2zm7.4 0h3a8 8 0 0 1 0 2h-3a17 17 0 0 0 0-2zM9.3 15h5.4c-.5 3-1.8 5-2.7 5s-2.2-2-2.7-5z"/></svg>
        www.HarborlineRestoration.example
      </li>
    </ul>
  </section>

  <section class="card card-back" aria-label="Business card back">
    <div class="back-brand">Harborline Restoration</div>
    <p class="tagline">Specializing in Water Damage Restoration</p>
  </section>
</body>
</html>
```